Healthy Snack Bar Wrapper Design

We are passionate about delivering healthy and tasty treats that are Raw, Organic, Preservative Free, Gluten Free, have No Added Sugar and No Additives!
In this project we are looking for a design for a new healthy food product to be launched soon in Australia. The packaging will be a bar wrapper made from foil that will be hot sealed, with a front and a back.
The snack is a raw, organic and healthy treat made predominantly with nuts, and will come in 3 initial flavours:
- Black Forest (Sour Cherry and Choc)
- Plum Fandango (Banana, Apricot and Blueberry)
- Zestivelle (Pineapple, Passionfruit and Kiwi)
The product name is NibbleMoss, which does not currently have a logo. We are happy to have this as a simple written component of the initial design at the top of the packaging, perhaps within an circle, square or oval.
The typeface used for the names and the main ingredients should be fun.
The overall design should be very simple and make use of minimal colours. Our preferences are to have a plain colour for the background, such as light organic brown or white, with an eye catching colour that can be used to define the flavour, but should not be too vibrant.
We do not want to have an 3 dimensional images or objects. Nor do we want to have product images and any imagery should be only to give the impression of the flavours within rather than an image of the flavour. Finally, we do not want to have gradients included in the design.
The final design should communicate healthy, tasty and fun!
Examples of inspiration designs are attached in the files.
Main Information:
- The front should comprise of the following information:
-- NibbleMoss
-- Flavour name (such as Black Forest)
-- Main Ingredients (Sour Cherry and Choc) (This is optional)
-- Portion size (60g)
-- Message (This is optional)
--- 0% Additives
--- 60% Nuts
--- 100% Natural
- The back needs to have space for the following information:
-- Nutritional Information
-- Barcode
-- Ingredients
-- Contact information
- Wrapper Dimensions
-- Width: 14cm
-- Height: 15cm
- Bar Dimensions
-- Width: 3cm
-- Height: 10cm
-- Depth: 2.5cm
Target Market(s)
People who want to have a healthy tasty treat
Colors
Designer to choose colors to be used in the design.
Requirements
Must have
- Main Information:
- - The front should comprise of the following information:
- -- NibbleMoss
- -- Flavour name (such as Black Forest)
- -- Main Ingredients (Sour Cherry and Choc) (This is optional)
- -- Portion size (60g)
- -- Message (This is optional)
- --- 0% Additives
- --- 60% Nuts
- --- 100% Natural
- - The back needs to have space for the following information:
- -- Nutritional Information
- -- Barcode
- -- Ingredients
- -- Contact information
- - Wrapper Dimensions
- -- Width: 14cm
- -- Height: 15cm
- - Bar Dimensions
- -- Width: 3cm
- -- Height: 10cm
- -- Depth: 2.5cm
Should not have
- We do not want to have an 3 dimensional images or objects. Nor do we want to have product images and any imagery should be only to give the impression of the flavours within rather than an image of the flavour. Finally, we do not want to have gradients included in the design.

```html
<!DOCTYPE html>
<html lang="en">
<head>
<meta charset="utf-8">
<title>NibbleMoss Bar Wrappers</title>
<link rel="stylesheet" href="https://fonts.googleapis.com/css2?family=Caveat+Brush&display=swap">
<style>
  :root {
    --page: #ffffff;
    --foil: #f6f6f4;
    --brand: #e0683a;
    --plum-main: #6f8fc4;
    --plum-accent: #e8a224;
    --plum-art: #efd458;
    --zest-main: #9bbd2d;
    --zest-accent: #e3b412;
    --zest-art: #ece7a6;
    --forest-main: #4a0a1e;
    --forest-accent: #e0542a;
    --forest-art: #4a0a1e;
  }
  * { margin: 0; padding: 0; box-sizing: border-box; }
  html, body { width: 1200px; height: 1000px; overflow: hidden; background: var(--page); }
  body { position: relative; font-family: "Caveat Brush", cursive; }

  .wrapper {
    position: absolute;
    top: 118px;
    width: 290px;
    height: 772px;
    color: var(--main);
  }
  .wrapper--plum   { left: 97px;  --main: var(--plum-main);   --accent: var(--plum-accent);   --art: var(--plum-art); }
  .wrapper--zest   { left: 465px; --main: var(--zest-main);   --accent: var(--zest-accent);   --art: var(--zest-art); }
  .wrapper--forest { left: 832px; --main: var(--forest-main); --accent: var(--forest-accent); --art: var(--forest-art); }

  .wrapper__body {
    position: absolute;
    top: 8px; bottom: 8px; left: 0; right: 0;
    background: var(--foil);
  }
  .wrapper__crimp { position: absolute; left: 0; width: 290px; height: 8px; display: block; }
  .wrapper__crimp--top { top: 0; }
  .wrapper__crimp--bottom { bottom: 0; transform: scaleY(-1); }
  .wrapper__seal {
    position: absolute; left: 0; right: 0; height: 30px;
    border-bottom: 1px solid #ebebe8;
  }
  .wrapper__seal--top { top: 8px; }
  .wrapper__seal--bottom { bottom: 8px; border-bottom: none; border-top: 1px solid #ebebe8; }

  .flavour-art {
    position: absolute;
    top: 8px; left: 0; right: 0; height: 300px;
    background: var(--art);
    opacity: 0.85;
  }

  .brand-name {
    position: absolute;
    top: 318px; left: 0; right: 0;
    text-align: center;
    font-size: 19px;
    color: var(--brand);
    letter-spacing: 0.5px;
  }

  .flavour-name {
    position: absolute;
    top: 352px; left: 0; right: 0;
    text-align: center;
    line-height: 0.9;
  }
  .flavour-name__main { display: block; font-size: 96px; }
  .flavour-name__sub  { display: block; font-size: 58px; }

  .claims { position: absolute; top: 490px; left: 0; right: 0; height: 150px; color: var(--accent); }
  .claim { position: absolute; line-height: 1; white-space: nowrap; }
  .claim--big { font-size: 42px; }
  .claim--small { font-size: 23px; }
  .claim--zero      { left: 42px;  top: 10px; }
  .claim--additives { left: 108px; top: 12px; transform: rotate(-4deg); }
  .claim--sixty     { left: 60px;  top: 62px; }
  .claim--nuts      { left: 68px;  top: 102px; }
  .claim--hundred   { left: 152px; top: 40px; }
  .claim--natural   { left: 166px; top: 80px; transform: rotate(-4deg); }

  .ingredients {
    position: absolute;
    top: 666px; left: 0; right: 0;
    text-align: center;
    font-size: 20px;
  }
  .weight {
    position: absolute;
    top: 722px; left: 0; right: 0;
    text-align: center;
    font-size: 21px;
  }
</style>
</head>
<body>
  <svg width="0" height="0" style="position:absolute">
    <defs>
      <pattern id="crimp-teeth" width="12" height="8" patternUnits="userSpaceOnUse">
        <polygon points="0,8 6,0 12,8" fill="#f6f6f4"/>
      </pattern>
    </defs>
  </svg>

  <article class="wrapper wrapper--plum">
    <svg class="wrapper__crimp wrapper__crimp--top" viewBox="0 0 290 8"><rect width="290" height="8" fill="url(#crimp-teeth)"/></svg>
    <div class="wrapper__body"></div>
    <svg class="wrapper__crimp wrapper__crimp--bottom" viewBox="0 0 290 8"><rect width="290" height="8" fill="url(#crimp-teeth)"/></svg>
    <div class="wrapper__seal wrapper__seal--top"></div>
    <div class="wrapper__seal wrapper__seal--bottom"></div>
    <div class="flavour-art" role="img" aria-label="Halftone pattern of yellow, orange and blue dots suggesting banana, apricot and blueberry"></div>
    <div class="brand-name">NibbleMoss</div>
    <h2 class="flavour-name"><span class="flavour-name__main">plum</span><span class="flavour-name__sub">fandango</span></h2>
    <div class="claims">
      <span class="claim claim--big claim--zero">0%</span>
      <span class="claim claim--small claim--additives">additives!</span>
      <span class="claim claim--big claim--sixty">60%</span>
      <span class="claim claim--small claim--nuts">nuts!</span>
      <span class="claim claim--big claim--hundred">100%</span>
      <span class="claim claim--small claim--natural">natural</span>
    </div>
    <p class="ingredients">banana · apricot · blueberry</p>
    <p class="weight">60g</p>
  </article>

  <article class="wrapper wrapper--zest">
    <svg class="wrapper__crimp wrapper__crimp--top" viewBox="0 0 290 8"><rect width="290" height="8" fill="url(#crimp-teeth)"/></svg>
    <div class="wrapper__body"></div>
    <svg class="wrapper__crimp wrapper__crimp--bottom" viewBox="0 0 290 8"><rect width="290" height="8" fill="url(#crimp-teeth)"/></svg>
    <div class="wrapper__seal wrapper__seal--top"></div>
    <div class="wrapper__seal wrapper__seal--bottom"></div>
    <div class="flavour-art" role="img" aria-label="Fine starburst line pattern in yellow, green and pink suggesting pineapple, passionfruit and kiwi"></div>
    <div class="brand-name">NibbleMoss</div>
    <h2 class="flavour-name"><span class="flavour-name__main">zesti</span><span class="flavour-name__sub">velle</span></h2>
    <div class="claims">
      <span class="claim claim--big claim--zero">0%</span>
      <span class="claim claim--small claim--additives">additives!</span>
      <span class="claim claim--big claim--sixty">60%</span>
      <span class="claim claim--small claim--nuts">nuts!</span>
      <span class="claim claim--big claim--hundred">100%</span>
      <span class="claim claim--small claim--natural">natural</span>
    </div>
    <p class="ingredients">pineapple · passionfruit · kiwi</p>
    <p class="weight">60g</p>
  </article>

  <article class="wrapper wrapper--forest">
    <svg class="wrapper__crimp wrapper__crimp--top" viewBox="0 0 290 8"><rect width="290" height="8" fill="url(#crimp-teeth)"/></svg>
    <div class="wrapper__body"></div>
    <svg class="wrapper__crimp wrapper__crimp--bottom" viewBox="0 0 290 8"><rect width="290" height="8" fill="url(#crimp-teeth)"/></svg>
    <div class="wrapper__seal wrapper__seal--top"></div>
    <div class="wrapper__seal wrapper__seal--bottom"></div>
    <div class="flavour-art" role="img" aria-label="Dark cherry-coloured branching tree shapes with small orange berries suggesting sour cherry and chocolate"></div>
    <div class="brand-name">NibbleMoss</div>
    <h2 class="flavour-name"><span class="flavour-name__main">black</span><span class="flavour-name__sub">forest</span></h2>
    <div class="claims">
      <span class="claim claim--big claim--zero">0%</span>
      <span class="claim claim--small claim--additives">additives!</span>
      <span class="claim claim--big claim--sixty">60%</span>
      <span class="claim claim--small claim--nuts">nuts!</span>
      <span class="claim claim--big claim--hundred">100%</span>
      <span class="claim claim--small claim--natural">natural</span>
    </div>
    <p class="ingredients">sour cherry · chocolate</p>
    <p class="weight">60g</p>
  </article>
</body>
</html>
```